The 5 stages of grief experience

I'm an artist and I'm launching my art debut and i need a whole set of thing. I have the logo and the colors and the list of what I need:
Sponsorship proposal (I have the info to be pasted once design is ready)
Flyer for my art. It's about the 5 stages of grief and its like you go into a maze to go through each art instillation that takes you over each feeling, there is a lot of feelings and symmetry in the art.
Denial
Anger
Depression
Bargaining
Acceptance
Updates

We are rushing on this project if anyone is interested we need it asap Added Monday, March 6, 2017

Target Market(s)

Visual Art society

Font styles to use
Sans Serif

Colors
fee4d6
f8ba93
000000
5c5c5c
fbfbfb

Requirements
Must have
• Symmetry
• Feeling
• Strong message
• Bold
• An artistic idea I like a lot is a black and white moon changes and it's 5 different moons starting from a crescent ending in a full moon all next to each other or on top of each other and the phases underneath in small geometric font
Nice to have
• Softness
Should not have
• Femininity

```html
<!DOCTYPE html>
<html lang="en">
<head>
<meta charset="utf-8">
<title>LUNE Arts Event – Sponsorship</title>
<link rel="stylesheet" href="https://fonts.googleapis.com/css2?family=Saira:wght@300;500;600;700&display=swap">
<style>
  :root {
    --ink: #000000;
    --graphite: #5c5c5c;
    --paper: #fbfbfb;
    --mist: #e4e4e4;
    --peach: #f8ba93;
    --peach-soft: #fee4d6;
  }
  * { margin: 0; padding: 0; box-sizing: border-box; }
  html, body { width: 900px; height: 1200px; overflow: hidden; }
  body {
    font-family: "Saira", "Arial", sans-serif;
    color: var(--ink);
    background: radial-gradient(ellipse 75% 60% at 38% 30%, var(--paper) 0%, #f4f4f4 55%, var(--mist) 100%);
  }
  .sheet { position: relative; width: 900px; height: 1200px; }

  .wash { position: absolute; left: 0; top: 0; width: 900px; height: 1200px; }

  .header-ornament { position: absolute; top: 40px; height: 190px; width: 345px;
    background: linear-gradient(180deg, rgba(0,0,0,0.16), rgba(0,0,0,0.05)); }
  .header-ornament--left { left: 0; }
  .header-ornament--right { right: 0; }

  .brand { position: absolute; left: 398px; top: 57px; width: 106px; text-align: center; }
  .brand__disc { width: 106px; height: 106px; border-radius: 50%; background: var(--ink); }
  .brand__name { margin-top: 22px; font-weight: 300; font-size: 27px; letter-spacing: 5px;
    color: var(--graphite); line-height: 1; }

  .content { position: absolute; left: 108px; top: 328px; }
  .title { font-weight: 700; font-size: 45px; letter-spacing: 1px; line-height: 1; margin-bottom: 34px; }
  .section { margin-bottom: 34px; }
  .section__heading { font-weight: 600; font-size: 23px; line-height: 1; margin-bottom: 5px; }
  .section p { font-weight: 600; font-size: 13.5px; line-height: 15px; letter-spacing: 0.5px;
    text-align: justify; margin-bottom: 15px; }
  .section--winwin p { width: 572px; }
  .section--fit p { width: 442px; text-align: left; }
  .section--about p { width: 684px; margin-bottom: 0; }
  .bullet { font-size: 13px; line-height: 15px; font-weight: 700; }
</style>
</head>
<body>
<div class="sheet">
  <svg class="wash" viewBox="0 0 900 1200" role="img" aria-label="Soft peach watercolour wash">
    <defs>
      <filter id="softEdge" x="-20%" y="-20%" width="140%" height="140%">
        <feGaussianBlur stdDeviation="28"/>
      </filter>
    </defs>
    <g fill="#fdd6bb" filter="url(#softEdge)" opacity="0.9">
      <ellipse cx="690" cy="420" rx="230" ry="140"/>
      <ellipse cx="560" cy="620" rx="300" ry="190"/>
      <ellipse cx="430" cy="900" rx="360" ry="150"/>
      <ellipse cx="760" cy="760" rx="150" ry="200"/>
    </g>
  </svg>

  <div class="header-ornament header-ornament--left" role="img" aria-label="Row of crossed brush-stroke ornaments"></div>
  <div class="header-ornament header-ornament--right" role="img" aria-label="Row of crossed brush-stroke ornaments"></div>

  <div class="brand">
    <div class="brand__disc"></div>
    <div class="brand__name">LUNE</div>
  </div>

  <main class="content">
    <h1 class="title">experience the art ...</h1>

    <section class="section section--winwin">
      <h2 class="section__heading">Its a win-win</h2>
      <p>Sponsoring LUNE Arts Event provides you the unique opportunity to connect with the art community in Saudi Arabia, to build brand awareness and show your company’s support of an important cause: the arts!</p>
      <p>This event reaches a certain key audience segment and provides a fun, entertaining and inspiring way for you to help us reach the audience, VIPs and volunteers. Feel good about supporting our local arts, heritage and cultural organisations as you enjoy an unforgettable evening.</p>
    </section>

    <section class="section section--fit">
      <h2 class="section__heading">find your fit</h2>
      <p>Looking for the opportunity to become apart of one the most unique events of the year, to put your company name in front of hundreds of sophisticated attendees.</p>
      <p>Want to show your employees and investors a dedication to our community.</p>
      <p>Consider a sponsorship at LUNE Arts Event</p>
    </section>

    <section class="section section--about">
      <h2 class="section__heading">about the event</h2>
      <p>Being the top events of the year, art exhibitions and galleries are highly requested in Saudi. Hence, an event with two different types of artists decided to collaborate to host for the first time an interactive art event for the very first time in saudi. Artists Rana AlHarbi and Faisal AlOmar are the founders of the LUNE Arts Event and aim to portray art in a unique view to saudis art audience.</p>
      <div class="bullet">•</div>
      <p>Targeting all art enthusiasts, we allow them to enjoy the arts while being apart of it and get the chance to enjoy various art pieces that carry meaning about human emotions and social experiences. Furthermore, people that attend LUNE Arts Event will get the opportunity to enjoy the arts while enjoying good food, drinks, and mingle with Saudi’s finest art community.</p>
    </section>
  </main>
</div>
</body>
</html>
```